Top New England Restaurant Needs Website Redesign

We currently have a website, rmsbistro.com, but would like to redesign it. We are a casual upscale restaurant specializing in breakfast and lunch. We are one of the top rated restaurants in all of New England and would like our site to look like it as well. We'd love to have a blog/news section that will be updated weekly or so, as well as an email capture feature on the page.

The site will mostly be static, with lots of pictures (I'll take them and provide). The only part of the site that will get updated regularly is the blog and/or news (could be the same page).

Some restaurant websites I like are: www.corvintable.com, www.brassandoat.com,

Target Market(s)

Foodies, RM's Bistro customers,

Industry/Entity Type

Restaurant

Logo Text

RM's Bistro

Font styles to use
Sans Serif

Requirements
Must have
• Friendloop Like Box, Dinetip Box, Email capture, Blog/News, About Us page, Contact page

```html
<!DOCTYPE html>
<html lang="en">
<head>
<meta charset="utf-8">
<title>RM's Bistro</title>
<link href="https://fonts.googleapis.com/css2?family=Josefin+Sans:wght@300;400;600;700&family=Poiret+One&family=Montserrat:wght@300;400;600&family=Dancing+Script:wght@600&display=swap" rel="stylesheet">
<style>
:root{
  --cyan:#1ba8d4;
  --cyan-dark:#1590b8;
  --ink:#333;
  --grey:#6a6a6a;
  --light:#eeeff1;
  --dark:#3d3d3d;
  --darker:#2b2b2b;
  --white:#fff;
}
*{margin:0;padding:0;box-sizing:border-box}
html,body{width:1200px;height:2872px;overflow:hidden;background:var(--white)}
body{position:relative;font-family:"Montserrat",sans-serif;color:var(--ink)}
.abs{position:absolute}

/* hero */
.hero{left:0;top:0;width:1200px;height:600px;background:linear-gradient(135deg,#6d5a49 0%,#8a7560 35%,#3c3a38 60%,#c9a24a 100%)}
.nav{left:175px;top:16px;width:955px;height:64px;background:rgba(0,0,0,.55);display:flex;align-items:center;justify-content:space-around;font-family:"Josefin Sans",sans-serif;font-size:15px;letter-spacing:1.5px;color:var(--white)}
.nav span.sep{opacity:.7}
.nav .active{border-bottom:2px solid var(--cyan);padding-bottom:10px;margin-top:12px}
.brand-box{left:383px;top:190px;width:382px;height:290px;background:rgba(40,40,40,.55)}
.brand{left:383px;top:245px;width:382px;text-align:center;font-family:"Josefin Sans",sans-serif;font-weight:700;font-size:44px;color:var(--white);letter-spacing:1px}
.tagline{left:415px;top:335px;width:318px;height:42px;background:rgba(255,255,255,.9);color:var(--cyan);font-family:"Josefin Sans",sans-serif;font-size:16px;letter-spacing:4px;text-align:center;line-height:44px;white-space:nowrap}
.hero-dots{left:560px;top:558px;display:flex;gap:10px}
.hero-dots i{width:12px;height:12px;border-radius:50%;border:2px solid var(--white);display:block}
.hero-dots i.on{background:var(--white)}

/* enjoy */
.enjoy{left:0;top:630px;width:1200px;text-align:center;font-family:"Josefin Sans",sans-serif;font-weight:700;font-size:48px;letter-spacing:10px;color:var(--cyan)}
.feature-main{left:163px;top:756px;width:389px;height:271px;background:linear-gradient(160deg,#c98a3a,#7b4a22 55%,#e6e2da)}
.feature-small-a{left:568px;top:868px;width:191px;height:159px;background:linear-gradient(160deg,#e9e4dc,#b86b2a 60%,#6b8a3c)}
.feature-small-b{left:772px;top:868px;width:204px;height:159px;background:linear-gradient(160deg,#d3e6f0,#a7672e 55%,#5d8a3a)}
.feature-title{left:574px;top:750px;width:430px;font-family:"Poiret One",sans-serif;font-size:38px;line-height:44px;letter-spacing:3px;color:var(--grey)}
.round-arrow{width:30px;height:30px}

/* story */
.story-photo{left:612px;top:1065px;width:588px;height:410px;background:linear-gradient(120deg,#d9d4cf,#c6b9ae 40%,#b34a3a 80%,#6e8b3d)}
.story-panel{left:622px;top:1148px;width:528px;height:272px;background:rgba(255,255,255,.75)}
.story-heading{left:112px;top:1165px;font-size:26px;color:var(--cyan);font-family:"Josefin Sans",sans-serif;letter-spacing:2px}
.story-heading .script{font-family:"Dancing Script",cursive;font-size:48px;letter-spacing:0}
.story-heading .with{font-size:18px;margin:0 8px}
.story-text{left:112px;top:1218px;width:480px;font-size:15.5px;line-height:27px;color:var(--grey);text-align:justify}
.story-text a{color:var(--cyan);text-decoration:none}
.perk{left:660px;width:460px}
.perk-title{margin-left:60px;font-family:"Josefin Sans",sans-serif;font-weight:600;font-size:17px;letter-spacing:1px;color:var(--ink)}
.perk-text{margin-left:60px;margin-top:10px;font-size:14px;line-height:22px;color:var(--grey)}
.perk-icon{left:0;top:14px;width:40px;height:40px}

/* menu */
.menu-title{left:0;top:1522px;width:1200px;text-align:center;font-family:"Josefin Sans",sans-serif;font-weight:600;font-size:38px;letter-spacing:10px;color:var(--ink)}
.menu-btn{left:520px;top:1585px;width:185px;height:32px;background:var(--cyan);color:var(--white);font-family:"Josefin Sans",sans-serif;font-size:18px;letter-spacing:2px;text-align:center;line-height:35px}
.dish{top:1659px;width:281px;height:462px}
.dish-a{left:134px;background:linear-gradient(180deg,#e7dfd2,#8b5a2b 45%,#5a3a20)}
.dish-b{left:450px;background:linear-gradient(180deg,#111,#b5762e 40%,#c23a1e 60%,#e7c13a 80%,#111)}
.dish-c{left:766px;background:linear-gradient(180deg,#556b3a,#8a5a2e 40%,#6b1f3a 60%,#3f3a35)}
.chev{top:1875px;font-size:54px;color:var(--ink);font-family:"Montserrat",sans-serif;font-weight:300}
.menu-dots{left:500px;top:2170px;display:flex;gap:12px}
.menu-dots i{width:14px;height:14px;border-radius:50%;background:var(--cyan);display:block}
.menu-dots i.on{background:var(--ink)}

/* testimonial & newsletter */
.lower{left:0;top:2252px;width:1200px;height:504px;background:var(--dark)}
.lower-photo{left:600px;top:2252px;width:600px;height:504px;background:linear-gradient(135deg,#4a4a4a,#6b6b6b 55%,#3a3a3a)}
.client-head{left:200px;top:2342px;display:flex;align-items:center;gap:8px;color:var(--cyan);font-family:"Josefin Sans",sans-serif;font-size:22px;letter-spacing:1px}
.avatar{left:252px;top:2410px;width:62px;height:62px;border-radius:50%;border:3px solid var(--white);background:linear-gradient(135deg,#c9a48b,#7a5a45)}
.client-name{left:100px;top:2500px;width:366px;text-align:center;color:var(--white);font-weight:600;font-size:15px;letter-spacing:1px}
.client-text{left:100px;top:2530px;width:366px;text-align:center;color:#e0e0e0;font-size:14px;line-height:23px}
.lower-chev{top:2475px;color:var(--cyan);font-size:40px;font-weight:300}
.stay{left:600px;top:2364px;width:600px;text-align:center;color:var(--cyan);font-family:"Josefin Sans",sans-serif;font-size:15px;letter-spacing:2px}
.news-title{left:600px;top:2396px;width:600px;text-align:center;color:var(--white);font-family:"Josefin Sans",sans-serif;font-weight:600;font-size:21px;letter-spacing:2px}
.email-field{left:740px;top:2462px;width:287px;height:38px;background:#5a5a5a;border:1px solid #777;color:#bbb;font-size:12px;letter-spacing:1px;line-height:38px;padding-left:14px}
.email-go{left:989px;top:2462px;width:38px;height:38px;background:var(--cyan);display:flex;align-items:center;justify-content:center}
.press{left:600px;top:2516px;width:600px;text-align:center;color:#ddd;font-size:14px}
.news-note{left:700px;top:2553px;width:400px;text-align:center;color:#ddd;font-size:14px;line-height:22px}

/* footer */
.footer{left:0;top:2756px;width:1200px;height:116px;background:var(--darker)}
.legal{left:96px;top:2800px;color:#ccc;font-size:12.5px;letter-spacing:.5px}
.social{left:828px;top:2795px;display:flex;gap:23px}
.social i{width:36px;height:36px;border-radius:50%;border:2px solid var(--cyan);display:block}
</style>
</head>
<body>

<!-- hero -->
<div class="abs hero" role="img" aria-label="Overhead photo of a wooden table with burgers, fries, salsa and nachos"></div>
<nav class="abs nav">
  <span class="active">HOME</span><span class="sep">|</span>
  <span>ABOUT US</span><span class="sep">|</span>
  <span>MENU</span><span class="sep">|</span>
  <span>OUR COFFEE</span><span class="sep">|</span>
  <span>NEWS</span><span class="sep">|</span>
  <span>CONTACT US</span>
</nav>
<div class="abs brand-box"></div>
<div class="abs brand">RM's Bistro</div>
<div class="abs tagline">THE HARBOR STACK</div>
<div class="abs hero-dots"><i class="on"></i><i></i><i></i></div>

<!-- enjoy / feature -->
<div class="abs enjoy">Enjoy</div>
<div class="abs feature-main" role="img" aria-label="Photo of a big burger with fries and salad on a plate"></div>
<div class="abs feature-title">INTRODUCING THE HARBOR STACK</div>
<div class="abs feature-small-a" role="img" aria-label="Photo of a cheeseburger with lettuce and tomato"></div>
<div class="abs feature-small-b" role="img" aria-label="Photo of a burger on a table outdoors"></div>
<svg class="abs round-arrow" style="left:113px;top:927px" viewBox="0 0 30 30"><circle cx="15" cy="15" r="13" fill="none" stroke="var(--cyan)" stroke-width="2"/><path d="M12 9l7 6-7 6z" fill="var(--cyan)"/></svg>
<svg class="abs round-arrow" style="left:1047px;top:927px" viewBox="0 0 30 30"><circle cx="15" cy="15" r="13" fill="none" stroke="var(--cyan)" stroke-width="2"/><path d="M18 9l-7 6 7 6z" fill="var(--cyan)"/></svg>

<!-- story band -->
<svg class="abs" style="left:0;top:1040px" width="1200" height="450" viewBox="0 0 1200 450">
  <path d="M0 40 Q150 0 300 30 T600 30 T900 25 T1200 20 L1200 420 Q1050 450 900 425 T600 430 T300 420 T0 435 Z" fill="var(--light)"/>
</svg>
<div class="abs story-photo" role="img" aria-label="Photo of fresh tomatoes, herbs and vegetables on a light table"></div>
<svg class="abs" style="left:600px;top:1040px" width="600" height="450" viewBox="0 0 600 450">
  <path d="M0 0 H600 V20 Q450 40 300 28 T0 36 Z" fill="var(--white)"/>
  <path d="M0 450 H600 V424 Q450 448 300 430 T0 436 Z" fill="var(--white)"/>
</svg>
<div class="abs story-panel"></div>
<div class="abs story-heading"><span class="script">Strat</span><span class="with">with</span>OUR STORY</div>
<p class="abs story-text">RM's Bistro is committed to superior food quality and cultivating a pleasurable and welcoming dining experience, akin to enjoying a home-cooked meal. We are truly excited to bring a fresh, new restaurant for breakfast and lunch to the City of Champions. From the warm welcome our guests <a>Read More</a></p>

<div class="abs perk" style="top:1172px">
  <svg class="abs perk-icon" viewBox="0 0 40 40"><circle cx="20" cy="20" r="12" fill="none" stroke="var(--cyan)" stroke-width="3"/><path d="M3 8v12M7 8v12M5 20v14M36 6v28" stroke="var(--cyan)" stroke-width="2.5"/></svg>
  <div class="perk-title">Fresh menu every day</div>
  <div class="perk-text">Lorem Ipsum is simply dummy text of the printing and typesetting industry. Lorem Ipsum has been the industry's standard</div>
</div>
<div class="abs perk" style="top:1306px">
  <svg class="abs perk-icon" viewBox="0 0 40 40"><path d="M6 26a14 14 0 0 1 28 0z" fill="none" stroke="var(--cyan)" stroke-width="3"/><path d="M3 30h34" stroke="var(--cyan)" stroke-width="3"/><circle cx="20" cy="10" r="2.5" fill="var(--cyan)"/></svg>
  <div class="perk-title">Exclusive Dishes</div>
  <div class="perk-text">Lorem Ipsum is simply dummy text of the printing and typesetting industry. Lorem Ipsum has been the industry's standard</div>
</div>

<!-- menu -->
<h2 class="abs menu-title">OUR MENU</h2>
<div class="abs menu-btn">see our menu</div>
<div class="abs dish dish-a" role="img" aria-label="Photo of a tall burger on a wooden board"></div>
<div class="abs dish dish-b" role="img" aria-label="Photo of a burger with flying layers on a black background"></div>
<div class="abs dish dish-c" role="img" aria-label="Photo of a beetroot veggie burger with greens"></div>
<div class="abs chev" style="left:96px">&#10216;</div>
<div class="abs chev" style="left:1078px">&#10217;</div>
<div class="abs menu-dots"><i class="on"></i><i></i><i></i><i></i><i></i><i></i><i></i><i></i></div>

<!-- testimonial & newsletter -->
<div class="abs lower" role="img" aria-label="Dark photo of a desk with a laptop and keyboard"></div>
<div class="abs lower-photo" role="img" aria-label="Dark photo of a chef at work in a kitchen"></div>
<div class="abs client-head">
  <svg width="26" height="26" viewBox="0 0 26 26"><circle cx="13" cy="13" r="11" fill="none" stroke="var(--cyan)" stroke-width="2"/><circle cx="9" cy="10" r="1.5" fill="var(--cyan)"/><circle cx="17" cy="10" r="1.5" fill="var(--cyan)"/><path d="M8 15q5 5 10 0" fill="none" stroke="var(--cyan)" stroke-width="2"/></svg>
  HAPPY CLIENT
</div>
<div class="abs avatar" role="img" aria-label="Portrait of the client"></div>
<div class="abs client-name">MARA LINDQVIST</div>
<p class="abs client-text">Lorem Ipsum is simply dummy text of the printing and typesetting industry. Lorem Ipsum has been the industry's standard dummy text ever since the 1500s</p>
<div class="abs lower-chev" style="left:50px">&#10216;</div>
<div class="abs lower-chev" style="left:530px">&#10217;</div>

<div class="abs stay">STAY UPDATE</div>
<div class="abs news-title">OUR NEWSLETTER</div>
<div class="abs email-field">YOUR EMAIL ADDRESS</div>
<div class="abs email-go"><svg width="16" height="16" viewBox="0 0 16 16"><path d="M4 2l8 6-8 6z" fill="var(--white)"/></svg></div>
<div class="abs press">press enter to submit</div>
<p class="abs news-note">Sign up to our newsletter, we promise send to email very soon</p>

<!-- footer -->
<footer class="abs footer"></footer>
<div class="abs legal">Site Map &nbsp;| &nbsp;Privacy &nbsp;| &nbsp;Terms Use &nbsp;| &nbsp;&copy; RM's Bistro All right reserved.</div>
<div class="abs social"><i></i><i></i><i></i><i></i><i></i></div>

</body>
</html>
```